ROVA Pty Ltd Business Card

Looking for a simple yet eye-catching double-sided business card design using my company logo on one side and contact details on the other.

Target Market(s)

Government

Industry/Entity Type

Communication Systems Engineering

Contact Information for Business Card

ROVA Pty Ltd

Requirements
Nice to have
• Would be great to have a QR code so details can be scanned into contacts

```html
<!DOCTYPE html>
<html lang="en">
<head>
<meta charset="utf-8">
<title>ROVA Pty Ltd Business Card</title>
<link href="https://fonts.googleapis.com/css2?family=Montserrat:wght@400;600;700&display=swap" rel="stylesheet">
<style>
  :root {
    --bg: #3b3b3c;
    --card-top: #2f3f46;
    --card-bottom: #1f2b31;
    --silver: #d4d6d8;
    --silver-dim: #8e979b;
    --rule: #b9bec1;
  }
  * { box-sizing: border-box; margin: 0; padding: 0; }
  html, body { width: 1200px; height: 1200px; overflow: hidden; }
  body {
    background: var(--bg);
    font-family: "Montserrat", sans-serif;
    color: var(--silver);
    position: relative;
  }
  .card {
    position: absolute;
    left: 220px;
    width: 760px;
    height: 440px;
    border-radius: 34px;
    background: radial-gradient(ellipse at 45% 35%, var(--card-top), var(--card-bottom) 85%);
    box-shadow: 0 18px 40px rgba(0,0,0,0.45);
    overflow: hidden;
  }
  .card-front { top: 70px; }
  .card-back { top: 620px; }

  .brand {
    position: absolute;
    display: flex;
    align-items: center;
    gap: 18px;
  }
  .brand-dot {
    border-radius: 50%;
    border: 3px solid var(--silver);
  }
  .brand-name {
    font-weight: 600;
    letter-spacing: 0.04em;
    color: var(--silver);
    line-height: 1;
  }
  .card-front .brand { left: 210px; top: 70px; }
  .card-front .brand-dot { width: 64px; height: 64px; }
  .card-front .brand-name { font-size: 84px; }

  .card-back .brand { left: 50%; top: 50%; transform: translate(-50%, -50%); gap: 30px; }
  .card-back .brand-dot { width: 110px; height: 110px; border-width: 4px; }
  .card-back .brand-name { font-size: 140px; }

  .rule { position: absolute; height: 1.5px; background: var(--rule); }
  .rule-main { left: 340px; right: 90px; top: 232px; }
  .rule-name { left: 70px; width: 260px; top: 320px; }

  .person { position: absolute; left: 70px; top: 262px; }
  .person-name { font-size: 30px; font-weight: 700; letter-spacing: 0.01em; line-height: 1; }
  .person-role { font-size: 16px; color: var(--silver-dim); letter-spacing: 0.06em; margin-top: 4px; }

  .contact-list { position: absolute; list-style: none; }
  .contact-list li {
    display: flex;
    align-items: flex-start;
    gap: 12px;
    font-size: 19px;
    line-height: 1.25;
    margin-bottom: 10px;
  }
  .contact-list svg { flex: none; width: 22px; height: 22px; margin-top: 1px; fill: none; stroke: var(--silver); stroke-width: 1.8; }
  .contact-left { left: 70px; top: 340px; }
  .contact-right { left: 400px; top: 250px; }
</style>
</head>
<body>

<section class="card card-front" aria-label="Card front with contact details">
  <div class="brand">
    <span class="brand-dot"></span>
    <span class="brand-name">ROVA</span>
  </div>

  <div class="rule rule-main"></div>

  <div class="person">
    <p class="person-name">FULL NAME</p>
    <p class="person-role">POSITION</p>
  </div>
  <div class="rule rule-name"></div>

  <ul class="contact-list contact-left">
    <li>
      <svg viewBox="0 0 24 24"><path d="M5 3h4l2 5-3 2a11 11 0 0 0 6 6l2-3 5 2v4a2 2 0 0 1-2 2A17 17 0 0 1 3 5a2 2 0 0 1 2-2z"/></svg>
      <span>(000) 000 0000</span>
    </li>
    <li>
      <svg viewBox="0 0 24 24"><rect x="2" y="5" width="20" height="14" rx="1"/><path d="M2 6l10 7 10-7"/></svg>
      <span>admin@rova.com.au</span>
    </li>
  </ul>

  <ul class="contact-list contact-right">
    <li>
      <svg viewBox="0 0 24 24"><circle cx="12" cy="12" r="10"/><path d="M2 12h20M12 2c3 3 3 17 0 20M12 2c-3 3-3 17 0 20"/></svg>
      <span>www.rova.com.au</span>
    </li>
    <li>
      <svg viewBox="0 0 24 24"><path d="M12 22s7-7 7-12a7 7 0 0 0-14 0c0 5 7 12 7 12z"/><circle cx="12" cy="10" r="2.5"/></svg>
      <span>42-44 Harlow St. Ferndale<br>NSW 2090, Australia</span>
    </li>
  </ul>
</section>

<section class="card card-back" aria-label="Card back with company name">
  <div class="brand">
    <span class="brand-dot"></span>
    <span class="brand-name">ROVA</span>
  </div>
</section>

</body>
</html>
```